依頼詳細
名刺裏面リニューアルのため、裏面のデザインをお願いいたします。
基本的にテキストのみの情報を掲載したいと思っています。
記載項目
①キャッチ
日本で唯一、新規営業に特化した営業支援会社です。

②弊社サービス紹介
・クヌーデル帳:
日本で唯一、新規営業に特化した営業ツール。
営業会社自ら、現場の声と使いやすさをもとにシステムを開発いたしました。

・企業リスト作成:
どんな営業活動も、まずはベストの営業先の見極めから。
社内、そしてWEBのデータを収集・分析を行ない、結果につながる、確度の高い企業リストを作成いたします。

・FAX集客支援:
中小企業、BtoBには非常に有効なFAXの原稿作成、またFAX配信を代行いたします。

③グループ会社一覧(社名の記載のみでかまいません)
・株式会社クレモアリス
・株式会社ミルベーナ
・ポルカノート株式会社
・株式会社ヴェルモンテ
・ハルネス株式会社
・株式会社ロザミオ
・株式会社エピフォルム
・華嶺泰股份有限公司(PELM ON RIVA CO.,LTD)
希望イメージ
シンプル 複雑
単色 カラフル
暗い 明るい
日常 高級
遊び心 厳粛
未来的 伝統的
女性的 男性的
希望する色
黒のテキストを希望します
納品ファイル
• 高解像度JPG (.jpg)
• イラストレーター形式 (.ai)
• フォトショップ形式 (.psd)
• PNG形式 (.png)
補足説明
添付にて参考までに名刺表面と既存の裏面データを送付します
当選者決定後のデータ入稿時ですが、以下の2点をお願いできますでしょうか。
------------------
①文字のアウトライン前のデータと、アウトライン済みのデータの2種類をお送
りください。
②jpg、pdfなどの見本データを一緒にお送りください。
------------------

またデザインにロゴ画像を使用していただいているご提案を当選とさせていただいた際には、
別途ロゴ画像データをお渡しいたしますので、入稿前に調整をお願いさせていただければと思います。
■ 選んだ理由

表面と並べた見たときのバランスの良さが一番のポイントとなりました。
また各コンテンツを読みやすく配置していただいており、営業の現場でもツールとして使いやすいのではないかと思ったことが選択の理由です。

■ 提案者全員のお礼・コメント

このたびは私どもの案件に多くのご提案をいただきありがとうございました。
素晴らしい提案が多く、選定に悩んでしまい、お時間をとってしまい申し訳ありませんでした。

今後もこのようなかたちでコンペを行うこともあるかと思いますが、また機会がありましたらぜひよろしくお願いいたします。

```html
<!DOCTYPE html>
<html lang="ja">
<head>
<meta charset="utf-8">
<title>名刺裏面</title>
<link rel="stylesheet" href="https://fonts.googleapis.com/css2?family=Cormorant+Garamond:wght@400&family=Noto+Sans+JP:wght@700&family=Noto+Serif+JP:wght@400;500&display=swap">
<style>
  :root {
    --paper: #ffffff;
    --ink: #1a1a1a;
    --ghost: #ececec;
  }
  * { margin: 0; padding: 0; box-sizing: border-box; }
  html, body {
    width: 776px; height: 1200px; overflow: hidden;
    background: var(--paper);
  }
  .card {
    position: relative;
    width: 776px; height: 1200px;
    background: var(--paper);
    color: var(--ink);
    font-family: "Noto Serif JP", serif;
    overflow: hidden;
  }
  .ghost-word {
    position: absolute;
    font-family: "Cormorant Garamond", serif;
    color: var(--ghost);
    line-height: 1;
    white-space: nowrap;
    z-index: 0;
  }
  .ghost-service { left: 95px; top: 230px; font-size: 150px; }
  .ghost-group { left: 120px; top: 860px; font-size: 170px; }

  .catch {
    position: absolute; top: 40px; left: 0; width: 100%;
    text-align: center; z-index: 1;
  }
  .catch-line { display: block; font-size: 33px; line-height: 62px; }
  .catch-main { font-size: 45px; font-weight: 500; line-height: 66px; }

  .services {
    position: absolute; left: 122px; top: 318px; width: 560px; z-index: 1;
  }
  .service { margin-bottom: 24px; }
  .service-title {
    font-family: "Noto Sans JP", sans-serif;
    font-weight: 700; font-size: 28px; line-height: 44px;
  }
  .service-text { font-size: 23.5px; line-height: 44px; white-space: nowrap; }

  .group-list {
    position: absolute; left: 130px; top: 948px; z-index: 1;
    display: grid; grid-template-columns: 260px 260px;
    font-size: 21px; line-height: 36px; list-style: none;
  }
  .group-list li { white-space: nowrap; }
  .group-list .en { padding-left: 18px; }
</style>
</head>
<body>
<main class="card">
  <div class="ghost-word ghost-service" aria-hidden="true">Service</div>
  <div class="ghost-word ghost-group" aria-hidden="true">Group</div>

  <header class="catch">
    <span class="catch-line">日本で唯一、</span>
    <span class="catch-line catch-main">新規営業に特化した</span>
    <span class="catch-line">営業支援会社です。</span>
  </header>

  <section class="services">
    <div class="service">
      <h2 class="service-title">■クヌーデル帳</h2>
      <p class="service-text">日本で唯一、新規営業に特化した営業ツール。<br>営業会社自ら、現場の声と使いやすさをもとにシステムを<br>開発いたしました。</p>
    </div>
    <div class="service">
      <h2 class="service-title">■企業リスト作成</h2>
      <p class="service-text">どんな営業活動も、まずはベストの営業先の見極めから。<br>社内、そしてWEBのデータを収集・分析を行ない、結果<br>につながる、確度の高い企業リストを作成いたします。</p>
    </div>
    <div class="service">
      <h2 class="service-title">■FAX集客支援</h2>
      <p class="service-text">中小企業、BtoBには非常に有効なFAXの原稿作成、また<br>FAX配信を代行いたします。</p>
    </div>
  </section>

  <ul class="group-list">
    <li>・株式会社クレモアリス</li>
    <li>・ハルネス株式会社</li>
    <li>・株式会社ミルベーナ</li>
    <li>・株式会社ロザミオ</li>
    <li>・ポルカノート株式会社</li>
    <li>・株式会社エピフォルム</li>
    <li>・株式会社ヴェルモンテ</li>
    <li>・華嶺泰股份有限公司</li>
    <li></li>
    <li class="en">(PELM ON RIVA CO.,LTD)</li>
  </ul>
</main>
</body>
</html>
```